Brochure Design Project

Hi I just need a brochure put together over 4 - 5 pages.
I will send you the logo, pictures, about us, services, and any other information. I just need it put together in a clean crisp professional way.
Front page should have logo and the first photo i upload of this building with contact details
T :1300 562 071
M: 0438217096
F :1900 347 615
E: enquiries@harbourquarrycraft.com.au
Second page should have services which you can find on my website www.harbourquarrycraft.com.au
Second page should have a list of previous work which you can find on the website www.harbourquarrycraft.com.au
Third page should have about us with our photos which you can find on the website. www.harbourquarrycraft.com.au
Fourth page should have a page with photos of previous work which you can find on the website and i will upload some photos on here.
Reason: Want to get some feedback from friends and make a few changes.
Target Market(s)
Builders in sydney.
Some residential customers aswell
Industry/Entity Type
Building
Requirements
Must have
- Double banded golden border running around the edge of each page.
1300 562 071 number visible on every page on top right or left corner.

```html
<!DOCTYPE html>
<html lang="en">
<head>
<meta charset="utf-8">
<title>Harbour Quarrycraft – Brochure Spread</title>
<link href="https://fonts.googleapis.com/css2?family=Roboto+Condensed:wght@300;400;700&display=swap" rel="stylesheet">
<style>
  :root {
    --backdrop: #8e8a86;
    --paper: #ffffff;
    --ink: #4a4440;
    --ink-soft: #7d7772;
    --heading: #3d3530;
    --gold-deep: #e2b62a;
    --gold-mid: #f1d36a;
    --gold-light: #fbf0c4;
    --card: #ececec;
    --sandstone-dark: #c9a776;
    --sandstone-light: #eadcc1;
  }
  * { box-sizing: border-box; margin: 0; padding: 0; }
  html, body {
    width: 1200px; height: 850px; overflow: hidden;
    background: var(--backdrop);
    font-family: "Roboto Condensed", Arial, sans-serif;
    color: var(--ink);
  }
  .spread {
    position: absolute; left: 60px; top: 165px;
    width: 1080px; height: 520px;
    background: var(--paper);
    box-shadow: 0 6px 18px rgba(0,0,0,.35);
    display: flex;
  }
  .page { position: relative; width: 540px; height: 100%; overflow: hidden; }
  .page--left { background: linear-gradient(90deg, #fff 0, #fff 480px, #f3f3f3 540px); }
  .page--right { background: linear-gradient(90deg, #dcdcdc 0, #f4f4f4 30px, #fff 80px, #fff 100%); }

  /* Golden double band */
  .gold-band {
    position: absolute; top: 0; bottom: 0; width: 40px;
    background: linear-gradient(90deg, var(--gold-deep), var(--gold-mid) 45%, var(--gold-light));
  }
  .gold-band::before, .gold-band::after {
    content: ""; position: absolute; top: 0; bottom: 0; right: 7px; width: 3px; background: #fff;
  }
  .gold-band::after { right: 0; width: 2px; background: var(--gold-deep); }
  .gold-band--left { left: 0; }
  .gold-band--right { right: 0; transform: scaleX(-1); }

  .band-label {
    position: absolute; top: 22px; white-space: nowrap;
    font-size: 11px; line-height: 1; color: var(--heading);
    writing-mode: vertical-rl;
  }
  .band-label strong { font-weight: 700; }
  .band-label--left { left: 12px; transform: rotate(180deg); }
  .band-label--left strong { margin-top: 5px; }
  .band-label--right { right: 12px; }
  .band-label--right strong { margin-bottom: 5px; }

  h2 { font-weight: 300; font-size: 20px; line-height: 24px; color: var(--heading); letter-spacing: -.2px; }

  /* Services */
  .services { position: absolute; left: 70px; top: 40px; width: 190px; }
  .service-list { list-style: none; margin-top: 58px; }
  .service-list li { position: relative; padding-left: 10px; margin-bottom: 10px; }
  .service-list li::before {
    content: ""; position: absolute; left: 0; top: 5px; width: 4px; height: 4px;
    border-radius: 50%; background: var(--ink);
  }
  .service-title { display: block; font-weight: 700; font-size: 10.5px; color: var(--ink); }
  .service-text { display: block; font-size: 9.5px; line-height: 1.25; color: var(--ink-soft); }

  /* Previous work */
  .previous-work { position: absolute; left: 275px; top: 40px; width: 245px; }
  .work-list { list-style: none; margin-top: 46px; }
  .work-list li {
    position: relative; padding-left: 10px; margin-bottom: 5px;
    font-size: 9px; line-height: 1.25; color: var(--ink-soft);
  }
  .work-list li::before {
    content: ""; position: absolute; left: 0; top: 4px; width: 3px; height: 3px;
    border-radius: 50%; background: var(--ink);
  }

  /* About */
  .about { position: absolute; left: 32px; top: 40px; width: 232px; }
  .about-body { margin-top: 34px; }
  .about-body p { font-size: 8.5px; line-height: 1.3; color: var(--ink-soft); margin-bottom: 7px; }

  .team { position: absolute; left: 44px; top: 318px; width: 206px; }
  .team-card { display: flex; gap: 8px; background: var(--card); padding: 6px; margin-bottom: 10px; }
  .team-photo { flex: none; width: 46px; height: 50px; background: linear-gradient(180deg, #b98e73, #4e4a48); }
  .team-name { font-size: 7.5px; font-weight: 700; color: var(--heading); margin-bottom: 3px; }
  .team-bio { font-size: 6.5px; line-height: 1.35; color: var(--ink-soft); }

  /* Photo panel */
  .stone-photo {
    position: absolute; left: 270px; top: 0; right: 40px; bottom: 0;
    background:
      linear-gradient(180deg, rgba(255,255,255,.15), rgba(0,0,0,.05)),
      linear-gradient(155deg, var(--sandstone-light), var(--sandstone-dark) 55%, #e0cba6);
  }
  .stone-quote {
    position: absolute; left: 20px; width: 190px; top: 108px;
    text-align: center; color: #fff; font-weight: 300; font-size: 14px; line-height: 1.22;
  }
  .quote-mark { font-size: 26px; line-height: 0; vertical-align: -9px; font-weight: 700; opacity: .9; }
</style>
</head>
<body>
  <div class="spread">
    <section class="page page--left">
      <div class="gold-band gold-band--left"></div>
      <div class="band-label band-label--left">Harbour Quarrycraft <strong>1300 562 071</strong></div>

      <div class="services">
        <h2>Our services</h2>
        <ul class="service-list">
          <li><span class="service-title">Heritage Restoration</span><span class="service-text">We completely re-vamp any stone building matching all original stones and finishes to the very last detail.</span></li>
          <li><span class="service-title">Feature Walls and Retaining Walls</span><span class="service-text">We build feature walls and retaining walls.</span></li>
          <li><span class="service-title">Commercial Services</span><span class="service-text">With our experience there's no job too big or too small.</span></li>
          <li><span class="service-title">Residential Services</span><span class="service-text">We undertake all types of residential projects. Visit the Residential Portfolio section on our website for some examples of our work.</span></li>
          <li><span class="service-title">Stone Veneer</span><span class="service-text">By selecting and using the highest quality stone available we create a finish tailored completely to our clients' needs.</span></li>
          <li><span class="service-title">Other Services</span><span class="service-text">We are able to provide many other services including epoxy patching/stone imitation, steps, arches, marble and granite fixing, mechanical fixing, paving and pointing.</span></li>
        </ul>
      </div>

      <div class="previous-work">
        <h2>Previous work</h2>
        <ul class="work-list">
          <li>Quayside Gallery of Modern Art – Restoration/Granite Marble Fixing/Repointing (Holdfast Builders)</li>
          <li>Merrow Court – Restoration (public works)</li>
          <li>Ridgeford Court House – Construction (public works)</li>
          <li>Jubilee Fields Park – Restoration (public works)</li>
          <li>Wharfside Road – The Landing – Restoration (Harbour Works Board)</li>
          <li>Carrow House Hostel – Restoration (Housing Trust)</li>
          <li>Vice-Regal House – Restoration (public works)</li>
          <li>Eastvale Technical College – Restoration (public works)</li>
          <li>Harbour Institute of Technology – Epoxy Patching (public works)</li>
          <li>Vice-Regal House – Repointing and Fixing (public works)</li>
          <li>Crown Botanic Gardens – (public works)</li>
          <li>Harbour University – New Stonework and Restoration (Harbour Uni)</li>
          <li>Tallis Park – Bayside Shire</li>
          <li>Innovation Park – Marden St</li>
          <li>Fountain Restoration – Harbour Uni</li>
          <li>No 9 Garnet St – Atrium – Lorne Vasey &amp; Assoc</li>
        </ul>
      </div>
    </section>

    <section class="page page--right">
      <div class="about">
        <h2>About us</h2>
        <div class="about-body">
          <p>Callum Brennock has been working both in London and Sydney over the last 15 years, following a family tradition started by his father Peter back in the 1960s. Callum served his apprenticeship in Sydney under the watchful eye of his father Peter. Once qualified, Callum subsequently worked as a freelance stonemason, where his skills were soon to be acknowledged and sought after by many of the established stone masons both in Sydney and London.</p>
          <p>Callum decided Sydney needed not only the services of a firm of first class stone masons, but a company who would understand Sydney's heritage, a company that was prepared to listen. This is when Harbour Quarrycraft was established.</p>
          <p>A combined 65 years of industry experience, Peter and Callum use the finest materials and embody good old-fashioned values to ensure each assignment undertaken produces results of true distinction.</p>
        </div>
      </div>

      <div class="team">
        <div class="team-card">
          <div class="team-photo" role="img" aria-label="Portrait photo of the managing director"></div>
          <div>
            <div class="team-name">Callum Brennock I Managing Director</div>
            <div class="team-bio">Callum is a second generation stonemason and business owner. With over 15 years of stonemasonry experience and training both locally and internationally, Callum prides himself on his ability to find out exactly what his clients need, and overdeliver time after time.</div>
          </div>
        </div>
        <div class="team-card">
          <div class="team-photo" role="img" aria-label="Portrait photo of the director"></div>
          <div>
            <div class="team-name">Peter Brennock I Director</div>
            <div class="team-bio">Peter Brennock has over 50 years in the building industry, a master mason from London. Major projects included a number of prestige buildings and monuments.</div>
          </div>
        </div>
      </div>

      <div class="stone-photo" role="img" aria-label="Close-up photo of a dressed sandstone block wall">
        <p class="stone-quote"><span class="quote-mark">“</span>Our team are experts in all aspects of masonry. We work on a huge variety of projects. There is no stone job we can't do.<span class="quote-mark">”</span></p>
      </div>

      <div class="gold-band gold-band--right"></div>
      <div class="band-label band-label--right"><strong>1300 562 071</strong> Harbour Quarrycraft</div>
    </section>
  </div>
</body>
</html>
```